Interactive Children's Media Book Company Website Design

We need a website DESIGN (no coding required) for a new interactive children's media book company called Tovira Studios.

We develop high-quality interactive children's books for the Slate/Pocketphone that seeks to delight and inspire young and old alike. Our stories are filled with heart and spirit, and we seek to breathe magic back into books so that people fall back in love with reading.

Tovira means "butterfly" in Korean. It plays on the idea that a caterpillar metamorphoses into a butterfly - and in the same way, our readers are transformed through the journey of experiencing our interactive books.

We're looking for something based on the ATTACHED LOGO DESIGN for our company. A website that's professional, modern, fun and inviting; easy to read and not-cluttered, but still portraying the feeling of innocence and childhood.

We're looking for something that resonates the magical experience we want to create for our readers. Specific requirements on pages, tabs, content, etc are below.

Industry/Entity Type

It Company

Requirements
Nice to have
• There are 7 tabs on the Homepage of the website: HOME, GRANDPA, ABOUT US, CAREERS, NEWS, CONTACT US, SHOP. (But there is an extra page called THEIR GARDEN, which will be a sub-page under Grandpa).

HOME
• Would be great to have some key images of our book (3-4 screen shots) as the key focus of the homepage that automatically scroll through every few seconds. (Placeholder image attached). The images would link to the “Grandpa” page.
• Company logo (attached to brief) and slogan: “A new era of children’s media” quite prominent on page.
• Key text content to be on page: “Tovira means “butterfly” in Korean. Just as a caterpillar transforms into a butterfly, Tovira Studios takes the reader on an unforgettable journey of metamorphosis through our stories. We turn children’s books into a high-quality interactive experience on mobile platforms - breathing magic back into books, and inspiring people to fall back in love with reading. Through our unique characters full of heart and spirit, our stories delight and inspire young and old alike.”
• Chirper & Friendbook Like & Friendbook page link icons.
• Section on Latest News with a few of the latest entries.
• Section on latest sister images & comments that visitors have posted, which takes you to the “Their Garden” page.

GRANDPA
• The title for this page is “Grandpa Keeps a Secret Garden”
• There will be a little Slate/Pocketphone icon (placeholder attached) for this book.
• There will be a link to the App Shelf to buy the app book.
• Key text content on this page: “Our debut interactive media book is coming soon on the Slate and Pocketphone! “Grandpa Keeps a Secret Garden” touches on the beautiful and inextricable (albeit sometimes frustrating!) bond between sisters.”
• There will be a section on “Features” which lists all the various special features the app book includes.
• There will be a VidStream clip embedded into the page, which shows how the app book works.
• A section that says: “Do you have a sister who’s not like other sisters? Share a photo and tell us about her!” which links to the sub-page “Their Garden”.
• Under this, there may be the most recent few images submitted by the public, which when clicked on, would also link to the sub-page “Their Garden”.

THEIR GARDEN
• The main text on the page: “Do you have a sister who’s not like other sisters? Share a photo and tell us about her!”
• Main body of the page is a gallery of all the photos that have been submitted. If you click on each of the images, you get the comments that people have submitted with the photos.
• The page would also have a Submit Comments Form, where people can upload a picture of their sister(s) and write a comment to accompany the image.

ABOUT US
• Introductory text on page: “It was a chance conversation at Harbourview Terminal, where two friends discovered they shared a dream to create quality children's media. Both of them were excited by the possibilities of using new digital platforms to inspire and educate a younger generation. From that idea Tovira Studios was born. We seek to be the chrysalis of story telling - to inspire the hearts and minds of our generation, and generations to come.”
• Section to “Join the Mailing List” where they can put their email address in and submit.
• Bios of 2x people with photos (bios in word doc attached) (do not have photos yet).

CAREERS
• The main text on the page: “We are always on the lookout for talented people to join our team. If you are a writer, illustrator, animator, iOS/android developer, musician, creative-writing translator - or have something special to offer Tovira Studios - we are keen to hear from you. Send us a message through the Contact Us tab above.”

NEWS
• Regular News page, with blog-type entries.

CONTACT US
• Online submit Contact Us form
• The main text on page: “Our studio is based in the Marram Arts Hub, 14 Pellham Street, Ardlow, Wellington. Marram is a professional, creative collective - with four separate studios, gallery, and retail store. For more information on Marram, visit: http://www.marramhub.example.nz”
• “We would love to hear from you! Whether you have questions, ideas, comments, or just want to say hullo - please leave us a message and we will get back to you soon.”
• Including image of the premises (Marram image attached to brief).

SHOP
• Where visitors can purchase merchandise (t-shirts, mugs, etc) of the book/company.

```html
<!DOCTYPE html>
<html lang="en">
<head>
<meta charset="utf-8">
<title>Tovira Studios – Grandpa</title>
<link rel="stylesheet" href="https://fonts.googleapis.com/css2?family=Arimo:wght@400;700&family=Kalam:wght@400&display=swap">
<style>
  :root {
    --ink: #111111;
    --white: #ffffff;
    --purple-deep: #4a1a78;
    --purple: #622a9e;
    --purple-mid: #7a3cc0;
    --lavender: #a46ae6;
    --lavender-soft: #b98af0;
    --nav-top: #8d55d4;
    --yellow: #f5d33a;
    --grey-box: #c9c9c9;
    --grey-text: #555555;
    --logo-grey: #8a8a8a;
  }
  * { box-sizing: border-box; margin: 0; padding: 0; }
  html, body { width: 1200px; height: 900px; overflow: hidden; background: var(--white); }
  body { position: relative; font-family: "Arimo", Arial, sans-serif; color: var(--white); }

  .site { position: absolute; left: 54px; top: 100px; width: 1100px; height: 644px; border: 2px solid var(--ink); overflow: hidden; background: var(--purple); }
  .abs { position: absolute; }

  /* left column */
  .brand { left: 0; top: 0; width: 296px; height: 136px; background: var(--white); display: flex; align-items: center; gap: 14px; padding-left: 20px; }
  .brand-dot { width: 60px; height: 60px; border-radius: 50%; background: var(--lavender-soft); flex: none; }
  .brand-name { color: var(--logo-grey); font-size: 29px; font-weight: 400; letter-spacing: 1px; white-space: nowrap; }

  .features { left: 0; top: 136px; width: 296px; height: 100px; background: var(--lavender); text-align: center; padding-top: 10px; }
  .features h2 { font-size: 24px; font-weight: 700; letter-spacing: 1px; line-height: 28px; }
  .features p { font-size: 14px; font-weight: 700; line-height: 20px; margin-top: 4px; }

  .features-body { left: 0; top: 236px; width: 296px; height: 408px; background: linear-gradient(160deg, var(--purple-deep) 0%, var(--purple) 60%, var(--purple-mid) 100%); }
  .lorem { font-size: 10px; line-height: 20px; }
  .features-body .lorem { position: absolute; left: 82px; top: 30px; width: 150px; line-height: 21px; }

  .video { left: 68px; top: 422px; width: 166px; height: 142px; background: #e6e6ee; border: 3px solid #2c1950; }
  .video-screen { left: 10px; top: 12px; width: 140px; height: 96px; background: #cfd0d8; }
  .video-play { left: 58px; top: 36px; }
  .video-bar { left: 10px; top: 116px; width: 140px; height: 8px; background: #9b9ca8; }
  .app-help { left: 68px; top: 566px; width: 166px; height: 32px; display: flex; align-items: center; gap: 10px; padding-left: 6px; font-size: 15px; font-weight: 700; background: var(--purple-deep); }
  .app-help-square { width: 22px; height: 22px; background: #d9d9d9; border-radius: 3px; }

  /* navigation */
  .nav-top { left: 296px; top: 0; width: 804px; height: 20px; background: var(--nav-top); }
  .nav { left: 296px; top: 20px; width: 804px; height: 66px; background: var(--purple-deep); }
  .nav-item { position: absolute; top: 12px; font-size: 14px; font-weight: 700; transform: translateX(-50%); white-space: nowrap; }
  .nav-current { position: absolute; left: 114px; top: 4px; width: 96px; height: 62px; background: var(--lavender); }
  .nav-sub { position: absolute; left: 114px; top: 40px; width: 96px; text-align: center; font-size: 14px; font-weight: 700; border-top: 2px solid var(--purple-deep); padding-top: 6px; }

  /* centre column */
  .announce-band { left: 296px; top: 86px; width: 460px; height: 50px; background: var(--purple); }
  .sun { left: 332px; top: 118px; }
  .announce { left: 376px; top: 132px; width: 380px; height: 50px; background: var(--purple-deep); border: 2px solid var(--white); font-size: 15px; font-weight: 700; text-align: center; line-height: 20px; padding-top: 3px; }
  .announce .hl { color: var(--yellow); }

  .book { left: 296px; top: 136px; width: 460px; height: 400px; background: #050505; }
  .book-title { position: absolute; left: 0; width: 100%; top: 66px; text-align: center; font-size: 21px; font-weight: 700; letter-spacing: 0.5px; line-height: 26px; }
  .book-art { position: absolute; left: 60px; top: 118px; width: 130px; height: 130px; border: 3px solid #1d4fa8; background: linear-gradient(160deg, #f5a45a, #e8c28f 50%, #7ac0c8); }
  .store-badge { position: absolute; left: 270px; top: 144px; width: 160px; height: 44px; border-radius: 8px; background: #6e6e6e; border: 2px solid #bcbcbc; }
  .order { position: absolute; left: 270px; top: 204px; width: 160px; text-align: center; font-size: 15px; }
  .book-blurb { position: absolute; left: 40px; top: 272px; width: 390px; font-family: "Kalam", cursive; font-size: 19px; line-height: 24px; text-align: center; }

  .social { left: 296px; top: 536px; width: 460px; height: 108px; background: var(--lavender); }
  .social-head { position: absolute; top: 10px; font-size: 12px; font-weight: 700; color: var(--yellow); }
  .social-square { position: absolute; top: 46px; width: 36px; height: 36px; background: #3c5a99; }
  .social-btn { position: absolute; top: 48px; width: 96px; height: 34px; border-radius: 5px; background: #d7d7e0; border: 1px solid #888; }
  .social-round { position: absolute; top: 44px; width: 36px; height: 36px; border-radius: 50%; background: #e8eef6; }

  /* right column */
  .share-band { left: 756px; top: 86px; width: 344px; height: 92px; background: var(--purple); }
  .share { left: 756px; top: 136px; width: 344px; height: 108px; background: var(--lavender); padding: 10px 12px 0 56px; font-size: 18px; font-weight: 700; line-height: 22px; }
  .share-dot { left: 770px; top: 118px; width: 34px; height: 34px; border-radius: 50%; background: var(--lavender-soft); }
  .gallery { left: 756px; top: 244px; width: 344px; height: 372px; background: var(--white); }
  .pic { position: absolute; top: 32px; width: 116px; height: 116px; border: 2px solid var(--ink); background: var(--grey-box); color: var(--white); font-size: 13px; font-weight: 700; display: flex; align-items: center; justify-content: center; }
  .gallery .lorem { position: absolute; top: 180px; width: 130px; color: var(--grey-text); }
  .garden-bar { left: 756px; top: 616px; width: 344px; height: 28px; background: var(--purple); }
  .garden-tab { position: absolute; left: 110px; top: 2px; width: 120px; height: 26px; background: var(--lavender); font-size: 14px; font-weight: 700; text-align: center; line-height: 26px; }

  .caption { position: absolute; left: 0; width: 1200px; top: 784px; text-align: center; color: var(--ink); font-size: 24px; }
</style>
</head>
<body>
  <main class="site">
    <div class="abs brand"><span class="brand-dot"></span><span class="brand-name">Tovira Studios</span></div>

    <section class="abs features">
      <h2>FEATURES</h2>
      <p>Grandpa Keeps a Secret Garden<br>App Includes the Following:</p>
    </section>
    <section class="abs features-body">
      <p class="lorem">Lorem ipsum dolor sit amet, consectetur adipiscing elit. Suspendisse vehicula pretium sapien, non pellentesque nisl semper nec. Aenean ornare, augue eu egestas tincidunt.</p>
    </section>

    <div class="abs video" role="img" aria-label="Embedded video showing how the app book works">
      <div class="abs video-screen"></div>
      <svg class="abs video-play" width="44" height="44" viewBox="0 0 44 44"><rect width="44" height="44" fill="#8c8ea0"/><path d="M15 11 L33 22 L15 33 Z" fill="#e3c63a"/></svg>
      <div class="abs video-bar"></div>
    </div>
    <div class="abs app-help"><span class="app-help-square"></span>App Instructions</div>

    <div class="abs nav-top"></div>
    <nav class="abs nav">
      <div class="nav-current"></div>
      <span class="nav-item" style="left:50px">Home</span>
      <span class="nav-item" style="left:162px">Grandpa</span>
      <span class="nav-item" style="left:286px">About Us</span>
      <span class="nav-item" style="left:404px">Careers</span>
      <span class="nav-item" style="left:506px">News</span>
      <span class="nav-item" style="left:620px">Contact Us</span>
      <span class="nav-item" style="left:730px">Shop</span>
      <span class="nav-sub">Their Garden</span>
    </nav>

    <div class="abs announce-band"></div>
    <section class="abs book">
      <h1 class="book-title">GRANDPA - KEEPS A SECRET GARDEN</h1>
      <div class="book-art" role="img" aria-label="Book cover character illustration"></div>
      <div class="store-badge" role="img" aria-label="App Shelf download badge"></div>
      <p class="order">ORDER NOW</p>
      <p class="book-blurb">Grandpa Keeps a Secret Garden touches on the beautiful and inextricable (albeit sometimes frustrating) bond between sisters</p>
    </section>
    <svg class="abs sun" width="40" height="40" viewBox="0 0 40 40" aria-hidden="true">
      <g stroke="#f2c12e" stroke-width="3" stroke-linecap="round">
        <line x1="20" y1="2" x2="20" y2="8"/><line x1="20" y1="32" x2="20" y2="38"/>
        <line x1="2" y1="20" x2="8" y2="20"/><line x1="32" y1="20" x2="38" y2="20"/>
        <line x1="7" y1="7" x2="11" y2="11"/><line x1="29" y1="29" x2="33" y2="33"/>
        <line x1="33" y1="7" x2="29" y2="11"/><line x1="7" y1="33" x2="11" y2="29"/>
      </g>
      <circle cx="20" cy="20" r="10" fill="#f7d23e"/>
    </svg>
    <div class="abs announce"><span class="hl">Our Debut Interactive Media Book is</span><br>COMING SOON on Slate and Pocketphone</div>

    <section class="abs social">
      <span class="social-head" style="left:42px">LIKE OUR FRIENDBOOK PAGE</span>
      <span class="social-head" style="left:270px">FOLLOW US ON CHIRPER</span>
      <span class="social-square" style="left:42px"></span>
      <span class="social-btn" style="left:90px"></span>
      <span class="social-round" style="left:268px"></span>
      <span class="social-btn" style="left:316px"></span>
    </section>

    <div class="abs share-band"></div>
    <section class="abs share">Do you have a sister thats not like other sisters? Share a photo and tell us about her...</section>
    <div class="abs share-dot"></div>
    <section class="abs gallery">
      <div class="pic" style="left:32px" role="img" aria-label="Visitor submitted photo">Picture</div>
      <div class="pic" style="left:192px" role="img" aria-label="Visitor submitted photo">Picture</div>
      <p class="lorem" style="left:32px">Lorem ipsum dolor sit amet, consectetur adipiscing elit. Suspendisse vehicula pretium sapien, non pellentesque nisl semper nec. Aenean ornare, augue eu egestas tincidunt.</p>
      <p class="lorem" style="left:192px">Lorem ipsum dolor sit amet, consectetur adipiscing elit. Suspendisse vehicula pretium sapien, non pellentesque nisl semper nec. Aenean ornare, augue eu egestas tincidunt.</p>
    </section>
    <div class="abs garden-bar"><span class="garden-tab">THEIR GARDEN</span></div>
  </main>

  <p class="caption">Grandpa Page</p>
</body>
</html>
```